Whitmore Business Card Design

The name of the business is Dara Whitmore, CPA LLC
The service that we offer is Accounting, Tax & Consulting Services. I need it to have the following items:
Dara Whitmore, Principal
Phone Number
Email Address
Physical Address

I have attached the company logo, one in black and one in white. Please provide a design in black background and the other in white background. Please include "Accounting, Tax & Consulting Services". I want the business card to be clean and very professional.

```html
<!DOCTYPE html>
<html lang="en">
<head>
<meta charset="utf-8">
<title>Dara Whitmore, CPA LLC — Business Cards</title>
<link href="https://fonts.googleapis.com/css2?family=Montserrat:wght@400;500;600&display=swap" rel="stylesheet">
<style>
  :root {
    --backdrop: #3a3a3c;
    --card-dark: #3d3d3f;
    --emboss-deep: #2e2e30;
    --emboss-mid: #3b3b3d;
    --emboss-light: #505052;
    --card-light: #ffffff;
    --ink: #2f2f31;
    --ink-soft: #8a8a8c;
    --brand-red: #9b1c1f;
    --white: #ffffff;
  }
  * { box-sizing: border-box; margin: 0; padding: 0; }
  html, body { width: 1200px; height: 1095px; overflow: hidden; }
  body {
    background: var(--backdrop);
    font-family: "Montserrat", sans-serif;
    position: relative;
  }

  .card {
    position: absolute;
    width: 700px;
    height: 400px;
    border-radius: 3px;
    overflow: hidden;
    box-shadow: 0 18px 40px rgba(0,0,0,0.35);
  }

  /* Front (dark) */
  .card--front {
    left: 90px;
    top: 80px;
    background: var(--card-dark);
  }
  .card__emboss {
    position: absolute;
    inset: 0;
    background:
      radial-gradient(ellipse at 15% 70%, rgba(255,255,255,0.10) 0%, rgba(255,255,255,0) 45%),
      radial-gradient(ellipse at 85% 20%, rgba(0,0,0,0.25) 0%, rgba(0,0,0,0) 50%),
      linear-gradient(120deg, var(--emboss-light) 0%, var(--emboss-mid) 40%, var(--emboss-deep) 75%, var(--emboss-mid) 100%);
  }
  .card--front .lockup {
    position: absolute;
    left: 0; right: 0;
    top: 110px;
    display: flex;
    flex-direction: column;
    align-items: center;
  }
  .card--front .lockup__mark {
    width: 52px; height: 52px;
    background: var(--white);
    margin-bottom: 26px;
  }
  .card--front .lockup__name {
    font-weight: 500;
    font-size: 38px;
    letter-spacing: 1px;
    color: var(--white);
    text-transform: uppercase;
    white-space: nowrap;
  }
  .card--front .lockup__tagline {
    margin-top: 12px;
    font-weight: 500;
    font-size: 24px;
    letter-spacing: 3px;
    color: var(--ink-soft);
    text-transform: uppercase;
  }

  /* Back (white) */
  .card--back {
    left: 420px;
    top: 600px;
    background: var(--card-light);
  }
  .card--back .lockup {
    position: absolute;
    left: 60px;
    top: 62px;
  }
  .lockup__row { display: flex; align-items: center; gap: 16px; }
  .card--back .lockup__mark { display: block; background: var(--ink); width: 30px; height: 30px; }
  .card--back .lockup__name {
    font-weight: 500;
    font-size: 31px;
    letter-spacing: 1px;
    color: var(--ink);
    text-transform: uppercase;
    white-space: nowrap;
  }
  .card--back .lockup__tagline {
    font-weight: 500;
    font-size: 19px;
    letter-spacing: 3px;
    color: var(--ink-soft);
    text-transform: uppercase;
    margin-top: 6px;
    margin-left: 46px;
  }

  .contact-block {
    position: absolute;
    left: 60px;
    top: 168px;
    display: flex;
    align-items: center;
    gap: 22px;
  }
  .person { text-align: right; }
  .person__name {
    font-weight: 500;
    font-size: 30px;
    color: var(--ink);
    text-transform: uppercase;
    letter-spacing: 0.5px;
    white-space: nowrap;
  }
  .person__title {
    font-size: 17px;
    color: var(--brand-red);
    margin-top: 2px;
  }
  .divider { width: 1.5px; height: 118px; background: var(--ink); }
  .details { list-style: none; display: flex; flex-direction: column; gap: 8px; }
  .details li {
    display: flex; align-items: center; gap: 9px;
    font-size: 16px; color: var(--ink); letter-spacing: 0.3px;
    white-space: nowrap;
  }
  .details svg { width: 14px; height: 14px; fill: var(--brand-red); flex: none; }

  .service-band {
    position: absolute;
    left: 0; right: 0;
    bottom: 28px;
    height: 50px;
    background: var(--brand-red);
    color: var(--white);
    display: flex; align-items: center; justify-content: center;
    font-weight: 600;
    font-size: 20px;
    letter-spacing: 1.5px;
    text-transform: uppercase;
  }
</style>
</head>
<body>

  <section class="card card--front">
    <div class="card__emboss" role="img" aria-label="Tone-on-tone embossed repeating pattern of the company mark across the dark card"></div>
    <div class="lockup">
      <span class="lockup__mark"></span>
      <span class="lockup__name">Dara Whitmore, CPA, LLC</span>
      <span class="lockup__tagline">Certified Public Accountant</span>
    </div>
  </section>

  <section class="card card--back">
    <div class="lockup">
      <div class="lockup__row">
        <span class="lockup__mark"></span>
        <span class="lockup__name">Dara Whitmore, CPA, LLC</span>
      </div>
      <div class="lockup__tagline">Certified Public Accountant</div>
    </div>

    <div class="contact-block">
      <div class="person">
        <div class="person__name">Dara Whitmore</div>
        <div class="person__title">Principal</div>
      </div>
      <span class="divider"></span>
      <ul class="details">
        <li>
          <svg viewBox="0 0 24 24"><path d="M6.6 10.8a15.1 15.1 0 0 0 6.6 6.6l2.2-2.2a1 1 0 0 1 1-.25 11.4 11.4 0 0 0 3.6.57 1 1 0 0 1 1 1V20a1 1 0 0 1-1 1A17 17 0 0 1 3 4a1 1 0 0 1 1-1h3.5a1 1 0 0 1 1 1c0 1.25.2 2.45.57 3.57a1 1 0 0 1-.25 1z"/></svg>
          (855) 555-0147
        </li>
        <li>
          <svg viewBox="0 0 24 24"><path d="M2 5h20v14H2z M2 5l10 8 10-8" fill="none" stroke="#9b1c1f" stroke-width="2"/><path d="M2 5h20l-10 8z"/></svg>
          info@darawhitmorecpa.com
        </li>
        <li>
          <svg viewBox="0 0 24 24"><circle cx="12" cy="12" r="9" fill="none" stroke="#9b1c1f" stroke-width="2"/><path d="M3 12h18M12 3c3 3 3 15 0 18M12 3c-3 3-3 15 0 18" fill="none" stroke="#9b1c1f" stroke-width="1.6"/></svg>
          www.darawhitmorecpa.com
        </li>
        <li>
          <svg viewBox="0 0 24 24"><path d="M12 2a7 7 0 0 0-7 7c0 5.2 7 13 7 13s7-7.8 7-13a7 7 0 0 0-7-7zm0 9.5A2.5 2.5 0 1 1 12 6.5a2.5 2.5 0 0 1 0 5z"/></svg>
          1420 Harbor Ln, Austin, TX 78701
        </li>
      </ul>
    </div>

    <div class="service-band">Accounting, Tax &amp; Consulting Services</div>
  </section>

</body>
</html>
```